We need our website look and feel updated to match our brand

We are looking to update our website and a "where to buy" tab at the top of the website. The current look and feel is ok but needs a clean up. The task is as follows:
1. Update the current pages and add a page for "Where to Buy"
2. Update the product page to reflect our current products. ie we have only three products now. Undercoat Q, Undercoat R and VELMIST. This page will have very similar descriptions and at the bottom of each product will be a link to our SDS (safety data sheets).
3. Please visit our current website for the look and feel.
4. Use our New Taglines need to be included. "Always Cleaning. All the Time." "24/7 SAFE SURFACE PROTECTION" (Logo as well)
5. The HomePage will need a nice clean location to our corporate video. https://clipvanta.com/Rk3TpWq9ZxN (link for viewing) that will be the highlight and easy to access on the homepage.
Some examples of websites we like.
https://lumivera.com/
https://orvastrell.com/ (like the use of motion graphics in these)
Our focus claims are that our product is a surface cleaner and deodorizer. We would like to see variations in black, white background (Black header bar) and Gray backgrounds.
5+ page

```html
<!DOCTYPE html>
<html lang="en">
<head>
<meta charset="utf-8">
<title>Lustrane — Always Cleaning. All the Time.</title>
<link href="https://fonts.googleapis.com/css2?family=Poppins:wght@400;500;600;700&display=swap" rel="stylesheet">
<style>
:root{
  --yellow:#f4c20d;
  --gold:#b9960f;
  --black:#000;
  --panel:#151515;
  --text:#fff;
  --muted:#cfcfcf;
  --grey:#8a8a8a;
}
*{box-sizing:border-box;margin:0;padding:0}
html,body{width:1200px;height:5249px;overflow:hidden}
body{position:relative;background:var(--black);color:var(--text);font-family:"Poppins",sans-serif}
.abs{position:absolute}
.label{color:var(--yellow);font-size:13px;font-weight:600;text-transform:uppercase}
.heading{font-size:30px;font-weight:700;line-height:1.2}
.body-text{font-size:13px;line-height:23px;color:#e6e6e6}
.read-more{color:var(--yellow);font-size:15px;font-weight:700;text-transform:uppercase}
.photo{position:absolute}

/* header */
.hero{position:absolute;left:0;top:0;width:1200px;height:727px;background:radial-gradient(circle at 30% 60%,#2a2a2a,#0b0b0b 70%)}
.hero-photo{left:720px;top:0;width:480px;height:727px;background:linear-gradient(200deg,#e9e9e9 0%,#8a8a8a 35%,#3a2d26 70%,#111 100%)}
.logo{position:absolute;display:flex;align-items:center;gap:12px}
.logo-mark{width:40px;height:40px;border:5px solid var(--yellow)}
.logo-name{font-weight:600;color:#fff}
.nav{position:absolute;left:335px;top:58px;display:flex;gap:36px;font-size:14px;font-weight:600}
.nav .active{border-left:3px solid var(--yellow);border-top:3px solid var(--yellow);padding:4px 0 0 8px;margin-top:-7px}
.hero-title{left:114px;top:262px;font-size:62px;font-weight:700;line-height:76px}
.hero-title .accent{color:var(--yellow)}
.hero-sub{left:114px;top:424px;font-size:26px;font-weight:600}
.btn{background:var(--yellow);color:#000;font-weight:700;text-transform:uppercase;display:flex;align-items:center;justify-content:center}
.shop-btn{left:114px;top:495px;width:155px;height:41px;font-size:16px}

/* framed features */
.frame{position:absolute;border:3px solid var(--yellow)}

/* video */
.video-frame{left:100px;top:1911px;width:1000px;height:570px;border:2px solid #6e5a10}
.video-still{left:112px;top:1923px;width:976px;height:544px;background:linear-gradient(180deg,#dfe3e6 0%,#cfd6da 45%,#f1d77a 70%,#e9c94e 100%)}
.play{left:988px;top:2373px;width:98px;height:94px;background:#111;display:flex;align-items:center;justify-content:center}

/* products */
.center{position:absolute;left:0;width:1200px;text-align:center}
.card{position:absolute;top:2675px;width:305px;height:462px;background:var(--panel);text-align:center}
.card-img{position:absolute;left:24px;top:30px;width:257px;height:239px}
.card h3{position:absolute;top:290px;width:100%;font-size:20px;font-weight:600;text-transform:uppercase}
.card p{position:absolute;top:328px;left:30px;right:30px;font-size:12.5px;line-height:24px;color:#ddd}
.price{position:absolute;top:384px;width:100%;font-size:16px;color:var(--yellow)}
.price s{margin-right:12px}
.stars{position:absolute;top:416px;width:100%;font-size:12px;color:var(--yellow);letter-spacing:1px}
.sds{position:absolute;left:50px;top:98px;width:157px;height:40px;background:#fff;color:#000;font-size:10px;font-weight:600;display:flex;align-items:center;justify-content:center}

/* newsletter */
.news-band{left:0;top:3253px;width:1200px;height:459px;background:linear-gradient(90deg,#2a2a2a,#4b4a44 40%,#3a3833 70%,#2b2b2b)}
.news-box{left:198px;top:3300px;width:653px;height:361px;background:#050505}
.input{position:absolute;background:#fff;color:#777;font-size:13px;display:flex;align-items:center;padding-left:22px}

/* faq */
.faq{position:absolute;left:114px;width:442px;background:#fff;color:#111}
.faq h4{font-size:12.5px;font-weight:700;text-transform:uppercase;line-height:17px}
.faq p{font-size:12.5px;line-height:23px;color:#777;margin-top:4px}
.faq-toggle{position:absolute;right:18px;width:30px;height:30px;border-radius:50%;border:2px solid #eee;color:var(--yellow);font-size:22px;display:flex;align-items:center;justify-content:center;line-height:1}
.news-item{position:absolute;left:599px}
.news-img{position:absolute;left:0;top:0;width:151px;height:148px}
.news-text{position:absolute;left:171px;top:0;width:330px}
.news-text h5{font-size:15px;font-weight:600}
.news-text .date{font-size:13px;color:#ddd;margin:2px 0 10px}
.news-text p{font-size:13px;line-height:23px;color:#cfcfcf}
.news-text .read-more{font-size:13px;text-decoration:underline;display:block;margin-top:2px}

/* projects */
.projects-band{left:0;top:4318px;width:1200px;height:581px;background:linear-gradient(180deg,#1a1a1a,#2d2d2d 50%,#1c1c1c)}
.project{position:absolute;top:4502px;width:265px;height:316px;border:3px solid var(--yellow);background:#000}
.project-img{position:absolute;left:12px;top:12px;right:12px;height:236px}
.project-label{position:absolute;left:12px;right:12px;bottom:0;height:45px;background:#fff;color:#111;font-size:14px;font-weight:600;display:flex;align-items:center;justify-content:center;text-transform:uppercase}

/* footer */
.footer{left:0;top:4899px;width:1200px;height:277px;background:var(--gold)}
.foot-col h6{font-size:20px;font-weight:600;text-transform:uppercase;color:#fff;margin-bottom:18px}
.foot-links li{list-style:none;font-size:13px;font-weight:600;line-height:31px}
.foot-find li{list-style:none;display:flex;gap:14px;font-size:12.5px;line-height:21px;margin-bottom:12px}
.social{position:absolute;top:5091px;display:flex;gap:15px}
.social span{width:28px;height:28px;border-radius:50%;background:#fff}
.copyright{left:0;top:5176px;width:1200px;height:73px;background:#000;display:flex;align-items:center;justify-content:center;font-size:15px}
</style>
</head>
<body>

<!-- Hero -->
<section class="hero">
  <div class="photo hero-photo" role="img" aria-label="Hand holding a spray gun releasing a fine mist"></div>
  <div class="logo" style="left:92px;top:38px">
    <span class="logo-mark"></span><span class="logo-name" style="font-size:40px">Lustrane</span>
  </div>
  <nav class="nav">
    <span class="active">HOME</span><span>ABOUT US</span><span>WHERE TO BUY</span><span>OUR TECHNOLOGY</span><span>NEWS</span><span>FAQ</span><span>CONTACT</span>
  </nav>
  <h1 class="abs hero-title">Always Cleaning.<br><span class="accent">All the Time.</span></h1>
  <div class="abs hero-sub">24/7 Safe Surface Protection.</div>
  <a class="abs btn shop-btn">Shop Now</a>
</section>

<!-- About -->
<div class="frame" style="left:126px;top:858px;width:497px;height:374px"></div>
<div class="photo" style="left:181px;top:937px;width:328px;height:473px;background:linear-gradient(180deg,#2b4fb0,#c9ccd4 45%,#e8e8ea 75%,#3550b5)" role="img" aria-label="Gloved hand spraying a surface cleaner"></div>
<div class="abs" style="left:560px;top:855px;width:70px;height:380px;background:#000"></div>
<div class="abs" style="left:570px;top:924px;width:455px">
  <div class="label">About Us</div>
  <div class="heading" style="margin-top:4px">Real World Solution</div>
  <p class="body-text" style="margin-top:12px">The onset of COVID-19 has changed our lives forever. The current methods of cleaning surfaces are not sustainable. Cleaning the environment we live in with caustic UV-C light, ammonia-based cleaners and other harsh chemicals is wasteful. The moment you clean the surface and an infected person touches that surface again, it requires reapplication of your protective cleaners.</p>
  <div class="read-more" style="margin-top:14px">Read More</div>
</div>

<!-- How it works -->
<div class="frame" style="left:589px;top:1465px;width:499px;height:377px"></div>
<div class="abs" style="left:585px;top:1500px;width:120px;height:310px;background:#000"></div>
<div class="photo" style="left:705px;top:1291px;width:330px;height:471px;background:linear-gradient(180deg,#d5f1fb,#6bcbe8 45%,#2a8fc0 80%,#1e4f9a)" role="img" aria-label="Hospital operating room with surgical lights"></div>
<div class="abs" style="left:196px;top:1520px;width:450px;text-align:right">
  <div class="label">How It Works</div>
  <div class="heading" style="margin-top:4px">Lustrane Technology</div>
  <p class="body-text" style="margin-top:12px">The onset of COVID-19 has changed our lives forever. The current methods of cleaning surfaces are not sustainable. Cleaning the environment, we live in with caustic UV-C light, ammonia-based cleaners and other harsh chemicals is wasteful. The moment you clean the surface and an infected person touches that surface again it requires reapplication of whatever you are using to keep the surfaces clean and safe.</p>
  <div class="read-more" style="margin-top:12px">Read More</div>
</div>

<!-- Video -->
<div class="abs video-frame"></div>
<div class="photo video-still" role="img" aria-label="Animated scene of workers in protective suits spraying a café interior"></div>
<a class="abs play" aria-label="Play corporate video">
  <svg width="50" height="50" viewBox="0 0 50 50"><circle cx="25" cy="25" r="22" fill="none" stroke="#e53b2c" stroke-width="3"/><path d="M20 15 L34 25 L20 35 Z" fill="none" stroke="#e53b2c" stroke-width="3" stroke-linejoin="round"/></svg>
</a>

<!-- Products -->
<div class="center label" style="top:2567px">Our Products</div>
<div class="center heading" style="top:2592px">Lustrane Products</div>

<article class="card" style="left:114px">
  <div class="card-img" style="background:linear-gradient(180deg,#8d8881,#a8a49b 40%,#c9c39a 70%,#8e8a82)" role="img" aria-label="Jar of Undercoat Q"></div>
  <h3>Undercoat Q</h3>
  <p>Lustrane UV – Top Coat is applied on top of Lustrane UV – Binder.</p>
  <div class="price"><s>$ 45.00</s>$ 30.00</div>
  <div class="stars">★★★★☆</div>
</article>
<article class="card" style="left:448px">
  <div class="card-img" style="background:linear-gradient(180deg,#d9b520,#e8c52a 50%,#d2ae1e)" role="img" aria-label="Jar of Undercoat R"><span class="sds">VIEW SAFETY DATA SHEETS</span></div>
  <h3>Undercoat R</h3>
  <p>Lustrane Visible Light is applied is applied on top of Lustrane G -Binder.</p>
  <div class="price"><s>$ 45.00</s>$ 30.00</div>
  <div class="stars">★★★★☆</div>
</article>
<article class="card" style="left:782px">
  <div class="card-img" style="background:linear-gradient(180deg,#8b8682,#a6a29b 40%,#cfc79a 70%,#8b8782)" role="img" aria-label="Jar of VELMIST"></div>
  <h3>VELMIST</h3>
  <p>Lustrane UV Binder Part A and B are combined in a 50/50 mix ratio.</p>
  <div class="price"><s>$ 45.00</s>$ 30.00</div>
  <div class="stars">★★★★☆</div>
</article>

<!-- Newsletter -->
<div class="photo news-band" role="img" aria-label="Row of coating jars in soft dark light"></div>
<div class="frame" style="left:114px;top:3255px;width:448px;height:453px"></div>
<div class="abs news-box"></div>
<div class="abs" style="left:244px;top:3372px;width:570px">
  <div class="label">Signup</div>
  <div class="heading" style="font-size:29px;margin-top:2px">Subscribe To Newsletter</div>
  <p style="font-size:12.5px;font-weight:600;line-height:24px;margin-top:10px">Lustrane has announced its plan to sell their unique Titanium Dioxide coatings in the United States. Lustrane is expanding its operations in these markets after using the materials in Japan for the past 25 years.</p>
</div>
<div class="input" style="left:244px;top:3546px;width:335px;height:41px">Email Address</div>
<a class="abs btn" style="left:579px;top:3546px;width:175px;height:41px;font-size:14px">Subscribe Now</a>

<!-- FAQ -->
<div class="abs" style="left:114px;top:3814px">
  <div class="label">Frequently Asked Questions</div>
  <div class="heading" style="margin-top:2px">Latest FAQ’S</div>
</div>
<div class="faq" style="top:3897px;height:171px;padding:20px 70px 0 22px">
  <h4>How can you claim yout TiO2 coating is permanent?</h4>
  <p>As it generates hydroxyl radicals &amp; superoxides, it is clear that it oxidizes all bacteria, microorganisms and any organic particles. But it should subsequently also get reduced as well.</p>
  <span class="faq-toggle" style="top:14px">+</span>
</div>
<div class="faq" style="top:4078px;height:51px;padding:17px 70px 0 22px">
  <h4>Does the TiO2 product have a shelf life?</h4>
  <span class="faq-toggle" style="top:10px">−</span>
</div>
<div class="faq" style="top:4139px;height:68px;padding:16px 70px 0 22px">
  <h4>Does the TiO2 product require mixing of other compounds?</h4>
  <span class="faq-toggle" style="top:19px">−</span>
</div>

<!-- News -->
<div class="abs" style="left:599px;top:3814px">
  <div class="label">News</div>
  <div class="heading" style="margin-top:2px">Latest News</div>
</div>
<div class="news-item" style="top:3895px">
  <div class="photo news-img" style="background:linear-gradient(135deg,#cfe2f3,#5a86b8 50%,#1f3f72)" role="img" aria-label="Laboratory glassware"></div>
  <div class="news-text">
    <h5>News Title 1</h5><div class="date">08 Feb 2022</div>
    <p>Lustrane has announced its plan to sell their unique Titanium Dioxide coatings in the United States. Lustrane is expanding its</p>
    <span class="read-more">Read More</span>
  </div>
</div>
<div class="news-item" style="top:4060px">
  <div class="photo news-img" style="background:linear-gradient(135deg,#5c74a8,#2c3b66 50%,#cfb39a)" role="img" aria-label="Scientist working with test tubes"></div>
  <div class="news-text">
    <h5>News Title 2</h5><div class="date">08 Feb 2022</div>
    <p>Lustrane has announced its plan to sell their unique Titanium Dioxide coatings in the United States. Lustrane is expanding its</p>
    <span class="read-more">Read More</span>
  </div>
</div>

<!-- Projects -->
<div class="photo projects-band" role="img" aria-label="Dim backdrop of a coating workshop"></div>
<div class="center label" style="top:4408px">Our Projects</div>
<div class="center heading" style="top:4432px">Latest Projects</div>
<div class="project" style="left:37px"><div class="project-img" style="background:linear-gradient(180deg,#d8f0fa,#5cb6e0 60%,#2a6fb0)" role="img" aria-label="Hospital operating room"></div><div class="project-label">University Hospital</div></div>
<div class="project" style="left:324px"><div class="project-img" style="background:linear-gradient(180deg,#3a3a3a,#b8b8b8 50%,#6a6a6a)" role="img" aria-label="Brushed metal restaurant signage"></div><div class="project-label">Grillhaus Volcano</div></div>
<div class="project" style="left:611px"><div class="project-img" style="background:linear-gradient(180deg,#e6e6e6,#bfc3c6 50%,#2f5f8a)" role="img" aria-label="Clean public restroom stalls"></div><div class="project-label">Odorless Bathrooms</div></div>
<div class="project" style="left:896px"><div class="project-img" style="background:linear-gradient(180deg,#6e2a22,#b85a48 40%,#d8d4d0 75%,#9a9590)" role="img" aria-label="Coated and uncoated test panel"></div><div class="project-label">Toll Booth Test</div></div>

<!-- Footer -->
<footer class="abs footer">
  <div class="logo" style="left:112px;top:72px">
    <span class="logo-mark" style="border-color:#fff;width:50px;height:50px"></span><span class="logo-name" style="font-size:42px">Lustrane</span>
  </div>
  <div class="abs foot-col" style="left:401px;top:60px">
    <h6>Quick Links</h6>
    <ul class="foot-links"><li>HOME</li><li>ABOUT US</li><li>WHER TO BUY</li><li>LATEST NEWS</li><li>OUR TECHNOLOGY</li></ul>
  </div>
  <div class="abs foot-col" style="left:623px;top:60px">
    <h6>Find Us</h6>
    <ul class="foot-find">
      <li><svg width="18" height="18" viewBox="0 0 18 18"><rect x="3" y="1" width="12" height="16" rx="2" fill="#fff"/><circle cx="9" cy="7" r="2" fill="#b9960f"/></svg><span>Lustrane,<br>Millbrook, CT USA</span></li>
      <li><svg width="18" height="18" viewBox="0 0 24 24"><path d="M6.6 10.8a15 15 0 006.6 6.6l2.2-2.2c.3-.3.7-.4 1-.2 1.1.4 2.3.6 3.6.6.6 0 1 .4 1 1V20c0 .6-.4 1-1 1A17 17 0 013 4c0-.6.4-1 1-1h3.5c.6 0 1 .4 1 1 0 1.3.2 2.5.6 3.6.1.3 0 .7-.2 1z" fill="#fff"/></svg><span>+1 555 014 7890</span></li>
      <li><svg width="18" height="18" viewBox="0 0 18 18"><rect x="1" y="3" width="16" height="12" fill="#fff"/><path d="M1 3 L9 10 L17 3" fill="none" stroke="#b9960f" stroke-width="1.5"/></svg><span>contactus@lustrane.com</span></li>
    </ul>
  </div>
  <div class="abs foot-col" style="left:862px;top:60px">
    <h6>Sign Up</h6>
  </div>
  <div class="input" style="left:862px;top:104px;width:225px;height:41px;justify-content:center;padding:0;color:#333;border-radius:4px">Email Address</div>
  <a class="abs" style="left:862px;top:160px;width:225px;height:41px;background:#fff;color:#111;border-radius:4px;font-size:13px;font-weight:700;display:flex;align-items:center;justify-content:center;gap:8px">SUBSCRIBE NOW
    <svg width="14" height="14" viewBox="0 0 14 14"><circle cx="7" cy="7" r="7" fill="#111"/><path d="M4 7h6M7.5 4.5L10 7l-2.5 2.5" stroke="#fff" stroke-width="1.4" fill="none"/></svg></a>
</footer>
<div class="social" style="left:141px"><span></span><span></span><span></span><span></span></div>
<div class="abs copyright">Copyright © 2022 Lustrane. All Rights Reserved.</div>

</body>
</html>
```